Young Balance Support Network

We need a poster explaining that some children live with a disability called Vestibular Disorder. Feel free to ask question. We want you to respect our color code, same as our logo.

Here is our website : http://www.ybsnetwork.org/

We need to sensibilise people about this disability for children.

Industry/Entity Type

Charity

Font styles to use
Serif

Requirements
Must have
• 1. our logo (with all our details) + one of the photo of Marek
• 2. design showing a child with a dizziness for exemple
• 3. a title saying : Aidez-nous à changer la vie des enfants vivant avec un problème vestibulaire
• 4.include the text attached (information flyer YBSN)
• Poster size : 24"X 36"
Should not have
• wheel chair

```html
<!DOCTYPE html>
<html lang="fr">
<head>
<meta charset="utf-8">
<title>Aidez-nous à changer la vie des enfants vivant avec un problème vestibulaire</title>
<link rel="stylesheet" href="https://fonts.googleapis.com/css2?family=Abril+Fatface&family=Marcellus&family=Playfair+Display+SC:wght@400&display=swap">
<style>
  :root {
    --teal: #1cb0a3;
    --pink: #e27f94;
    --pink-soft: #fbe3e8;
    --ink: #2a1a24;
    --navy: #1f3a5a;
    --sky: #4bb8e8;
    --orange: #f2a23a;
    --paper: #ffffff;
    --skin: #e2a495;
    --skin-light: #f1c7b8;
    --blanket: #f6f1f3;
    --lilac: #8a5a8a;
  }
  * { margin: 0; padding: 0; box-sizing: border-box; }
  html, body { width: 800px; height: 1200px; overflow: hidden; background: var(--paper); }
  .poster { position: relative; width: 800px; height: 1200px; background: var(--paper); overflow: hidden; }

  .hero-photo {
    position: absolute; left: 0; top: 540px; width: 800px; height: 660px; z-index: 1;
    background:
      radial-gradient(ellipse 150px 170px at 395px 360px, var(--skin-light) 0%, var(--skin) 55%, rgba(226,164,149,0.55) 78%, rgba(246,241,243,0) 100%),
      repeating-conic-gradient(from 0deg at 395px 360px, rgba(255,255,255,0.55) 0deg 14deg, rgba(220,205,215,0.35) 14deg 28deg),
      radial-gradient(ellipse 340px 320px at 395px 370px, var(--blanket) 50%, rgba(246,241,243,0.85) 75%, rgba(255,255,255,0) 100%),
      radial-gradient(ellipse 240px 330px at 40px 290px, rgba(138,90,138,0.85) 0%, rgba(160,120,160,0.45) 50%, rgba(255,255,255,0) 100%),
      radial-gradient(ellipse 420px 200px at 380px 600px, rgba(190,165,185,0.55) 0%, rgba(255,255,255,0) 100%),
      var(--paper);
    -webkit-mask-image: linear-gradient(to bottom, transparent 0%, #000 28%);
            mask-image: linear-gradient(to bottom, transparent 0%, #000 28%);
  }

  .title {
    position: absolute; top: 6px; left: 20px; width: 760px; z-index: 2;
    font-family: "Abril Fatface", serif; font-weight: 400;
    color: var(--teal); text-transform: uppercase; text-align: center;
    font-size: 37px; line-height: 44px; letter-spacing: 0.3px;
  }

  .block { position: absolute; z-index: 2; }
  .block-left { left: 29px; width: 369px; }
  .block-right { left: 418px; width: 363px; }
  .row-1 { top: 160px; }
  .row-2 { top: 321px; }

  .block h2 {
    font-family: "Playfair Display SC", serif; font-weight: 400;
    color: var(--pink-soft); -webkit-text-stroke: 0.8px var(--pink);
    font-size: 21px; line-height: 22px; text-transform: uppercase;
    letter-spacing: 0.6px;
    text-align: justify; text-align-last: center;
    margin-bottom: 22px;
  }
  .row-1.block-left h2 { margin-bottom: 36px; }
  .block p {
    font-family: "Marcellus", serif; color: var(--ink);
    font-size: 19.5px; line-height: 16.8px; text-align: justify; text-align-last: center;
    hyphens: manual;
  }

  .org {
    position: absolute; left: 544px; top: 634px; width: 230px; z-index: 2;
    display: flex; gap: 14px; align-items: flex-start;
  }
  .org-text { width: 140px; }
  .org-name {
    font-family: "Marcellus", serif; color: var(--navy);
    font-size: 14px; line-height: 15px; text-transform: uppercase; letter-spacing: 1px;
    margin-bottom: 12px;
  }
  .org-detail { font-family: "Marcellus", serif; font-size: 8px; line-height: 16px; letter-spacing: 0.5px; }
  .org-detail.web { color: var(--sky); }
  .org-detail.mail { color: var(--orange); }
  .org-detail.ccp { color: var(--sky); }
  .org-mark { width: 70px; height: 70px; border-radius: 50%; background: var(--sky); margin-top: 6px; flex: none; }
</style>
</head>
<body>
<main class="poster">
  <div class="hero-photo" role="img" aria-label="Photo of a crying newborn wrapped in a white blanket, with a spinning motion blur evoking dizziness"></div>

  <h1 class="title">Aidez-nous à changer la vie des enfants vivant avec un problème vestibulaire</h1>

  <section class="block block-left row-1">
    <h2>Qu'est-ce que le vestibule ?</h2>
    <p>C’est un organe sensoriel, pilier de votre équilibre, véritable 6ème sens situé dans l’oreille interne.</p>
  </section>

  <section class="block block-right row-1">
    <h2>Qu'est ce qu'une aréflexie vestibulaire ?</h2>
    <p>C’est l’absence complète de toute in&shy;formation vestibulaire. L’enfant a ainsi l’impression que tout vacille autour de lui, jour et nuit.</p>
  </section>

  <section class="block block-left row-2">
    <h2>Quelles en sont les con&shy;séquences pour l'enfant ?</h2>
    <p>Le développement moteur de l’enfant est retardé car il doit trouver des so&shy;lutions afin de construire son équili&shy;bre, stabiliser son regard et son corps. Certains apprentissages sont de véritables obstacles pour l’enfant : se représenter son propre corps, se situer dans l’espace qui l’entoure, in&shy;teragir avec les autres, communi&shy;quer, écrire, lire, manger, boire, marcher. Chacune de ces actions né&shy;cessitent des efforts considérables pour se concentrer quelques sec&shy;ondes ou minutes. Quand l’enfant réussit à effectuer l’une de ces ac&shy;tions, son comportement peut sem&shy;bler déroutant et bien trop souvent mal interprété par le grand public.</p>
  </section>

  <section class="block block-right row-2">
    <h2>Quel est le but de notre association ?</h2>
    <p>Notre association a pour but de pro&shy;mouvoir les troubles vestibulaires chez l’enfant, ses conséquences sur sa santé ainsi que celui de son en&shy;tourage et de soutenir ces enfants et leurs parents en leur offrant un espace de parole et des solutions concrètes pour soulager leur quoti&shy;dien. Notre association a également pour but de financer et promouvoir toute action de recherche scienti&shy;fique visant à aider les enfants ayant un trouble vestibulaire.</p>
  </section>

  <aside class="org">
    <div class="org-text">
      <div class="org-name">Young Balance Support Network</div>
      <div class="org-detail web">WWW.YBSNETWORK.ORG</div>
      <div class="org-detail mail">INFO@YBSNETWORK.ORG</div>
      <div class="org-detail ccp">CCP: 12-345678-9</div>
    </div>
    <div class="org-mark" aria-hidden="true"></div>
  </aside>
</main>
</body>
</html>
```